Tailbrook Website Design

Need a website for a Dog Grooiming business. Please make it simular to these:

https://www.furvanto.com
https://haulnorix.com
https://meadowpetrin.com
https://www.drivelumo.com/search/

```html
<!DOCTYPE html>
<html lang="en">
<head>
<meta charset="utf-8">
<title>Tailbrook – Dog Grooming</title>
<link href="https://fonts.googleapis.com/css2?family=Luckiest+Guy&family=Roboto:ital,wght@0,400;0,500;0,700;1,400&display=swap" rel="stylesheet">
<style>
:root{
  --teal:#6cc5d1;
  --teal-light:#9ad6df;
  --green:#35c165;
  --green-band:#2aa84c;
  --dark:#111;
  --text:#555;
  --footer:#3b3b3b;
  --white:#fff;
  --underline:#b9e3ea;
}
*{margin:0;padding:0;box-sizing:border-box}
html,body{width:1200px;height:3746px;overflow:hidden}
body{position:relative;font-family:'Roboto',Arial,sans-serif;color:var(--text);background:var(--white)}
.abs{position:absolute}
.display{font-family:'Luckiest Guy',Impact,'Arial Black',sans-serif;color:var(--dark);letter-spacing:1px;font-weight:400;line-height:1.1}
.rule{display:block;height:7px;border-radius:4px;background:var(--underline)}
.btn{position:absolute;background:var(--green);color:var(--white);font-weight:700;font-size:15px;display:flex;align-items:center;justify-content:center;gap:8px;border-radius:2px}
.btn .dot{width:13px;height:13px;border-radius:50%;background:var(--white);display:inline-flex;align-items:center;justify-content:center}

/* header */
.site-header{top:0;left:0;width:1200px;height:78px;background:var(--white)}
.brand{left:115px;top:20px;display:flex;align-items:center;gap:10px;font-family:'Luckiest Guy',Impact,sans-serif;font-size:30px;color:var(--teal)}
.brand .mark{width:30px;height:30px;border-radius:50%;background:var(--teal)}
.nav{left:390px;top:29px;display:flex;gap:29px;font-size:13px;font-weight:500;color:#222}
.nav .active{color:var(--teal);border-bottom:2px solid var(--teal);padding-bottom:6px}
.call{left:905px;top:17px;display:flex;gap:14px;align-items:center}
.call small{display:block;font-size:11px;font-weight:700;color:#222}
.call strong{display:block;font-size:22px;color:var(--green);font-weight:500}

/* hero */
.hero{top:78px;left:0;width:1200px;height:558px;background:linear-gradient(90deg,#a6dbe3,#7fc9d4)}
.hero-photo{left:140px;top:0;width:440px;height:558px;background:radial-gradient(ellipse at 50% 45%,#f4f4f2 0%,#dfe6e6 55%,rgba(170,215,222,0) 80%)}
.hero-tag{left:650px;top:150px;height:37px;padding:0 30px 0 34px;background:var(--green);color:var(--white);font-size:12px;font-weight:700;display:flex;align-items:center;clip-path:polygon(0 0,100% 0,92% 50%,100% 100%,0 100%)}
.hero-title{left:650px;top:206px;font-size:62px;line-height:66px;color:var(--white)}
.hero-text{left:650px;top:291px;width:460px;font-size:15px;font-weight:500;line-height:20px;color:var(--white)}

/* intro */
.intro-title{left:112px;top:760px;font-size:31px}
.intro-text{left:112px;top:848px;width:450px;font-size:15px;line-height:26px}
.intro-phone{left:112px;top:1012px;display:flex;align-items:center;gap:14px;font-size:21px;color:var(--green);font-weight:500}
.intro-phone .icon{width:34px;height:34px;border-radius:50%;background:var(--green);display:flex;align-items:center;justify-content:center}
.intro-photo{left:650px;top:725px;width:480px;height:345px;background:radial-gradient(ellipse at 45% 55%,#c99a62 0%,#e8d6bf 40%,#6a8fc9 62%,rgba(255,255,255,0) 78%)}
.divider{left:0;top:1134px;width:1200px;height:1px;background:#e8e8e8}

/* services */
.section-title{width:1200px;left:0;text-align:center}
.svc{position:absolute;width:293px;height:224px}
.svc .back{position:absolute;inset:-8px -6px -4px -8px;background:#bfe8cf;transform:rotate(-1.5deg);border-radius:8px}
.svc .photo{position:absolute;inset:0;border-radius:8px;overflow:hidden}
.svc .caption{position:absolute;left:0;bottom:0;width:100%;height:64px;background:rgba(0,0,0,.55);color:var(--white);font-size:14px;text-align:center;padding-top:12px;line-height:18px;border-radius:0 0 8px 8px}
.svc .label{position:absolute;left:12px;top:13px;background:var(--green);color:var(--white);font-size:12px;font-weight:700;padding:6px 17px;border-radius:14px}

/* videos */
.video-band{top:1920px;left:0;width:1200px;height:318px;background:var(--teal)}
.video{left:278px;top:2062px;width:645px;height:379px;background:linear-gradient(120deg,#c8b9a4,#a0764a 45%,#3a3430 80%)}
.play{left:573px;top:2224px;width:56px;height:56px;border-radius:50%;background:#111;border:3px solid var(--white);display:flex;align-items:center;justify-content:center}

/* testimonials */
.quote-card{position:absolute;top:2622px;width:319px;height:240px;background:var(--white);box-shadow:0 0 8px rgba(0,0,0,.15);padding:24px 14px}
.quote-card.featured{background:var(--green);color:var(--white)}
.quote-card .q{font-family:'Luckiest Guy',Impact,sans-serif;font-size:40px;color:var(--teal);line-height:30px;height:30px}
.quote-card.featured .q{color:var(--white)}
.quote-card p{font-style:italic;font-size:14px;line-height:23px;margin-top:18px}
.quote-card .person{display:flex;align-items:center;gap:36px;margin-top:26px}
.quote-card .avatar{width:52px;height:52px;border-radius:50%;background:#cfd4d8}
.quote-card.featured .avatar{background:#a7dcb9}
.quote-card .name{font-size:14px;font-weight:500;color:var(--teal)}
.quote-card.featured .name{color:var(--white)}
.quote-card .role{font-size:14px}
.dots{left:572px;top:2920px;display:flex;gap:4px}
.dots span{width:9px;height:9px;border-radius:50%;background:var(--teal)}
.dots .on{background:var(--white);border:2px solid var(--teal)}

/* partners */
.seen{top:3009px;left:0;width:1200px;height:344px;background:var(--green-band)}
.partner{position:absolute;top:3175px;width:187px;height:98px;background:var(--white);display:flex;align-items:center;justify-content:center}
.partner span{width:70px;height:40px;background:#d6d6d6;border-radius:4px}

/* footer */
.footer{top:3353px;left:0;width:1200px;height:393px;background:var(--footer);color:var(--white)}
.fcol{position:absolute;top:87px;font-size:14px}
.fcol h4{font-size:13px;font-weight:700;margin-bottom:8px}
.fcol h4::after{content:"";display:block;width:24px;height:3px;background:var(--white);margin-top:8px}
.fcol li{list-style:none;height:34px;display:flex;align-items:center;gap:14px}
.fcol li i{width:14px;text-align:center;font-style:normal;font-size:12px}
.fcol li.indent{padding-left:28px}
.fline{left:110px;top:331px;width:980px;height:1px;background:#6a6a6a}
.copy{left:0;top:350px;width:1200px;text-align:center;font-size:15px}
</style>
</head>
<body>

<header class="abs site-header">
  <div class="abs brand"><span class="mark"></span>TAILBROOK</div>
  <nav class="abs nav">
    <span class="active">HOME</span><span>ABOUT US</span><span>OUR SERVICES</span><span>REVIEWS</span><span>CONTACT US</span>
  </nav>
  <div class="abs call">
    <svg width="22" height="36" viewBox="0 0 22 36"><rect x="2" y="2" width="18" height="32" rx="3" fill="none" stroke="#35c165" stroke-width="3"/><circle cx="11" cy="29" r="2" fill="#35c165"/></svg>
    <div><small>CALL US NOW</small><strong>1 555 014 2207</strong></div>
  </div>
</header>

<section class="abs hero">
  <div class="abs hero-photo" role="img" aria-label="White fluffy dog smiling, photographed against a teal background"></div>
  <div class="abs hero-tag">DOG GROOMING SERVICES</div>
  <h1 class="abs display hero-title">TAILBROOK</h1>
  <p class="abs hero-text">Sed ut perspiciatis unde omnis iste natus error sit voluptatem accusantium doloremque laudantium, totam rem aperiam,</p>
  <div class="btn" style="left:650px;top:358px;width:165px;height:51px">BOOK ONLINE <span class="dot"><svg width="7" height="7" viewBox="0 0 7 7"><path d="M1 3.5h5M3.5 1l2.5 2.5L3.5 6" stroke="#35c165" stroke-width="1.4" fill="none"/></svg></span></div>
</section>

<section>
  <h2 class="abs display intro-title">THE TAILBROOK SERVICES</h2>
  <span class="abs rule" style="left:112px;top:806px;width:138px"></span>
  <p class="abs intro-text">Sed ut perspiciatis unde omnis iste natus error sit voluptatem accusantium doloremque laudantium, totam rem aperiam, eaque ipsa quae ab illo inventore veritatis et quasi architecto beatae vitae dicta sunt explicabo. Nemo enim ipsam voluptatem quia voluptas sit aspernatur aut odit aut fugit</p>
  <div class="abs intro-phone"><span class="icon"><svg width="16" height="16" viewBox="0 0 16 16"><path d="M3 1l3 3-1.5 2a9 9 0 0 0 5.5 5.5L12 10l3 3-2 2C7 15 1 9 1 3z" fill="#fff"/></svg></span>1 555 014 2207</div>
  <div class="btn" style="left:337px;top:1003px;width:156px;height:44px;font-size:14px">BOOK ONLINE <span class="dot"><svg width="7" height="7" viewBox="0 0 7 7"><path d="M1 3.5h5M3.5 1l2.5 2.5L3.5 6" stroke="#35c165" stroke-width="1.4" fill="none"/></svg></span></div>
  <div class="abs intro-photo" role="img" aria-label="Two beagles beside a blue towel and a basket of grooming tools"></div>
  <div class="abs divider"></div>
</section>

<section>
  <h2 class="abs display section-title" style="top:1196px;font-size:31px">OUR SERVICES</h2>
  <span class="abs rule" style="left:528px;top:1244px;width:144px"></span>

  <div class="svc" style="left:119px;top:1306px"><div class="back"></div><div class="photo" role="img" aria-label="Small white dog getting a bath" style="background:linear-gradient(135deg,#6b5a4c,#c8b8a6 50%,#3b3029)"></div><span class="label">WATER BATH</span><div class="caption">Lorem ipsum dolor sit amet, consec<br>tetur adipiscing</div></div>
  <div class="svc" style="left:458px;top:1306px"><div class="back"></div><div class="photo" role="img" aria-label="Groomers feeding a small dog natural products" style="background:linear-gradient(135deg,#3f5a86,#a7a39b 50%,#2e3440)"></div><span class="label">NATURAL PRODUCTS</span><div class="caption">Lorem ipsum dolor sit amet, consec<br>tetur adipiscing</div></div>
  <div class="svc" style="left:796px;top:1306px"><div class="back"></div><div class="photo" role="img" aria-label="Groomer blow-drying a dog's coat" style="background:linear-gradient(135deg,#e6e0d8,#b0352e 45%,#c98c4b)"></div><span class="label">BLOW OUT</span><div class="caption">Lorem ipsum dolor sit amet, consec<br>tetur adipiscing</div></div>

  <div class="svc" style="left:119px;top:1582px"><div class="back"></div><div class="photo" role="img" aria-label="Groomer filing a small dog's nails" style="background:linear-gradient(135deg,#5d8fb0,#b98a6a 50%,#e8e8e8)"></div><span class="label">FILE NAILS</span><div class="caption">Lorem ipsum dolor sit amet, consec<br>tetur adipiscing</div></div>
  <div class="svc" style="left:458px;top:1582px"><div class="back"></div><div class="photo" role="img" aria-label="Small terrier having its teeth brushed" style="background:linear-gradient(135deg,#e9e6e1,#8a6b4e 50%,#d9d4cc)"></div><span class="label">CLEAN TEETH</span><div class="caption">Lorem ipsum dolor sit amet, consec<br>tetur adipiscing</div></div>
  <div class="svc" style="left:796px;top:1582px"><div class="back"></div><div class="photo" role="img" aria-label="Several dogs playing on green grass" style="background:linear-gradient(135deg,#6f8f3a,#4a3a2c 50%,#7fae3c)"></div><span class="label">BREED GROOM</span><div class="caption">Lorem ipsum dolor sit amet, consec<br>tetur adipiscing</div></div>
</section>

<section>
  <div class="abs video-band"></div>
  <h2 class="abs display section-title" style="top:1966px;font-size:31px;color:#fff">OUR VIDEOS</h2>
  <span class="abs rule" style="left:528px;top:2013px;width:144px;background:#fff"></span>
  <div class="abs video" role="img" aria-label="Pomeranian being groomed with scissors by a groomer"></div>
  <div class="abs play"><svg width="20" height="22" viewBox="0 0 20 22"><path d="M3 1l16 10L3 21z" fill="#35c165"/></svg></div>
</section>

<section>
  <h2 class="abs display section-title" style="top:2515px;font-size:31px">HERE'S WHAT PET PARENTS HAVE TO SAY</h2>
  <span class="abs rule" style="left:528px;top:2564px;width:144px"></span>

  <div class="quote-card" style="left:111px"><div class="q">“</div><p>Lorem ipsum dolor sit amet, consectetuadipiscing elit, sed do eiusmod tempor incididunt ut labore et dolore magna</p><div class="person"><span class="avatar"></span><div><div class="name">MARA QUILLON</div><div class="role">Businessman</div></div></div></div>
  <div class="quote-card featured" style="left:441px"><div class="q">“</div><p>Lorem ipsum dolor sit amet, consectetuadipiscing elit, sed do eiusmod tempor incididunt ut labore et dolore magna</p><div class="person"><span class="avatar"></span><div><div class="name">MARA QUILLON</div><div class="role">Businessman</div></div></div></div>
  <div class="quote-card" style="left:769px"><div class="q">“</div><p>Lorem ipsum dolor sit amet, consectetuadipiscing elit, sed do eiusmod tempor incididunt ut labore et dolore magna</p><div class="person"><span class="avatar"></span><div><div class="name">MARA QUILLON</div><div class="role">Businessman</div></div></div></div>

  <div class="abs dots"><span></span><span></span><span class="on"></span><span></span><span></span></div>
</section>

<section>
  <div class="abs seen"></div>
  <h2 class="abs display section-title" style="top:3068px;font-size:31px;color:#fff">AS SEEN ON</h2>
  <span class="abs rule" style="left:528px;top:3115px;width:144px;background:#fff"></span>
  <div class="partner" style="left:110px"><span></span></div>
  <div class="partner" style="left:308px"><span></span></div>
  <div class="partner" style="left:506px"><span></span></div>
  <div class="partner" style="left:705px"><span></span></div>
  <div class="partner" style="left:903px"><span></span></div>
</section>

<footer class="abs footer">
  <div class="fcol" style="left:120px"><h4>QUICK LINKS</h4><ul><li><i>»</i>Home</li><li><i>»</i>About Us</li><li><i>»</i>Services</li><li><i>»</i>Benefits</li><li><i>»</i>Contact Us</li></ul></div>
  <div class="fcol" style="left:350px"><h4>OTHER LINKS</h4><ul><li><i>»</i>Sitemap</li><li><i>»</i>FAQ</li><li><i>»</i>Terms &amp; Conditions</li><li><i>»</i>Privacy Policy</li><li><i>»</i>Help Service</li></ul></div>
  <div class="fcol" style="left:637px"><h4>CONTACT US</h4><ul>
    <li><i><svg width="10" height="14" viewBox="0 0 10 14"><path d="M5 0a5 5 0 0 1 5 5c0 4-5 9-5 9S0 9 0 5a5 5 0 0 1 5-5z" fill="#fff"/><circle cx="5" cy="5" r="2" fill="#3b3b3b"/></svg></i>42 Larkspur Row</li>
    <li class="indent">Brookfield</li>
    <li><i><svg width="13" height="13" viewBox="0 0 16 16"><path d="M3 1l3 3-1.5 2a9 9 0 0 0 5.5 5.5L12 10l3 3-2 2C7 15 1 9 1 3z" fill="#fff"/></svg></i>1 555 014 2207</li>
    <li><i><svg width="13" height="12" viewBox="0 0 13 12"><rect x="0" y="3" width="13" height="9" rx="1" fill="#fff"/><rect x="3" y="0" width="7" height="4" fill="#fff"/></svg></i>1 555 019 3348</li>
    <li><i><svg width="13" height="10" viewBox="0 0 13 10"><rect x="0.5" y="0.5" width="12" height="9" fill="none" stroke="#fff"/><path d="M1 1l5.5 4.5L12 1" fill="none" stroke="#fff"/></svg></i>hello@tailbrook.com</li>
  </ul></div>
  <div class="fcol" style="left:941px"><h4>FIND US ON</h4><ul>
    <li><i><svg width="10" height="10"><circle cx="5" cy="5" r="5" fill="#fff"/></svg></i>Chirpline</li>
    <li><i><svg width="10" height="10"><circle cx="5" cy="5" r="5" fill="#fff"/></svg></i>Snapframe</li>
    <li><i><svg width="10" height="10"><circle cx="5" cy="5" r="5" fill="#fff"/></svg></i>Friendwall</li>
    <li><i><svg width="10" height="10"><circle cx="5" cy="5" r="5" fill="#fff"/></svg></i>Clipstream</li>
  </ul></div>
  <div class="abs fline"></div>
  <div class="abs copy">© 2021 Tailbrook. All Rights Reserved</div>
</footer>

</body>
</html>
```